Building company buisness cards

We are looking for a sharp modern new look for our business cards.We are a New Zealand based company that specialises in house and land packages.We have attached a photo of the current logo and would like to see if it can be improved somehow if needed.We are open to any colours but we have chosen Black and White at this stage. Feel free to change the font and make the logo smarter looking.Play with the colours and see what looks best.We want a card that looks so good know one will want to throw it away!

Target Market(s)

Building profesonals, home buyers

Industry/Entity Type

Building

Contact Information for Business Card

Derek Haskins
0274930268
derekh@stonerange.co.nz

Font styles to use
Serif
Sans Serif

Colors

Designer to choose colors to be used in the design.

Requirements
Must have
• Just the logo on one side and details on the other
• Clean simple looking card
Nice to have
• Round corners and detail like raised or spot UV
• Something that stands out
Should not have
• To title needed, Director etc

```html
<!DOCTYPE html>
<html lang="en">
<head>
<meta charset="utf-8">
<title>Front of Business Card – Derek Haskins</title>
<link rel="stylesheet" href="https://fonts.googleapis.com/css2?family=PT+Sans:wght@400;700&display=swap">
<style>
  :root {
    --page-bg: #ffffff;
    --ink: #000000;
    --card-green: #008000;
    --frame-white: #ffffff;
    --ornament-gold: #f5c400;
    --name-fill: #5a5d5c;
    --name-edge: #1f2120;
    --contact-white: #ffffff;
  }
  * { margin: 0; padding: 0; box-sizing: border-box; }
  html, body {
    width: 1200px;
    height: 1003px;
    overflow: hidden;
    background: var(--page-bg);
  }
  .canvas {
    position: relative;
    width: 1200px;
    height: 1003px;
    font-family: "PT Sans", "Trebuchet MS", sans-serif;
  }
  .sheet-title {
    position: absolute;
    top: 124px;
    left: 0;
    width: 100%;
    text-align: center;
    font-size: 23px;
    font-weight: 400;
    color: var(--ink);
  }
  .card {
    position: absolute;
    left: 204px;
    top: 254px;
    width: 798px;
    height: 500px;
    border-radius: 28px;
    background: var(--card-green);
  }
  .card-frame {
    position: absolute;
    left: 29px;
    top: 29px;
    width: 741px;
    height: 442px;
    border: 3px solid var(--frame-white);
    border-radius: 30px;
  }
  .corner-ornament {
    position: absolute;
    left: 50px;
    top: 48px;
    width: 200px;
    height: 204px;
  }
  .holder-name {
    position: absolute;
    left: 200px;
    top: 178px;
    font-size: 56px;
    font-weight: 700;
    letter-spacing: 3px;
    line-height: 1;
    color: var(--name-fill);
    -webkit-text-stroke: 1.5px var(--name-edge);
    text-shadow:
      0 -1px 0 rgba(255,255,255,0.35),
      1px 2px 2px rgba(0,0,0,0.55);
  }
  .contact-list {
    position: absolute;
    left: 256px;
    top: 294px;
    list-style: none;
  }
  .contact-item {
    display: flex;
    align-items: center;
    height: 34px;
    margin-bottom: 30px;
    color: var(--contact-white);
    font-size: 24px;
  }
  .contact-icon {
    width: 42px;
    height: 34px;
    margin-right: 26px;
    flex: none;
  }
</style>
</head>
<body>
<main class="canvas">
  <h1 class="sheet-title">Front of Business Card</h1>

  <section class="card" aria-label="Business card front">
    <div class="card-frame"></div>

    <svg class="corner-ornament" viewBox="0 0 200 204" role="img" aria-label="Gold filigree scroll ornament in the top-left corner">
      <defs>
        <linearGradient id="ornamentTone" x1="0" y1="0" x2="1" y2="1">
          <stop offset="0" stop-color="#f5c400" stop-opacity="0.85"/>
          <stop offset="1" stop-color="#f5c400" stop-opacity="0.25"/>
        </linearGradient>
      </defs>
      <path d="M0 10 Q0 0 10 0 H190 Q200 0 200 10 V50 Q200 70 180 72 H80 Q72 72 72 80 V190 Q72 204 58 204 H10 Q0 204 0 194 Z" fill="url(#ornamentTone)"/>
    </svg>

    <p class="holder-name">Derek Haskins</p>

    <ul class="contact-list">
      <li class="contact-item">
        <svg class="contact-icon" viewBox="0 0 42 34" aria-hidden="true">
          <g fill="none" stroke="#ffffff" stroke-width="3" stroke-linejoin="round">
            <path d="M2 12 Q2 3 21 3 Q40 3 40 12 L40 14 L31 14 L31 9 L11 9 L11 14 L2 14 Z"/>
            <path d="M9 15 L33 15 L38 31 L4 31 Z"/>
            <circle cx="21" cy="23" r="4.5"/>
          </g>
        </svg>
        <span class="contact-text">0274930268</span>
      </li>
      <li class="contact-item">
        <svg class="contact-icon" viewBox="0 0 42 34" aria-hidden="true">
          <g fill="none" stroke="#ffffff" stroke-width="3" stroke-linejoin="round">
            <rect x="2" y="5" width="38" height="24" rx="1"/>
            <path d="M2 5 L21 19 L40 5"/>
            <path d="M2 29 L16 16 M40 29 L26 16"/>
          </g>
        </svg>
        <span class="contact-text">derekh@stonerange.co.nz</span>
      </li>
    </ul>
  </section>
</main>
</body>
</html>
```